Parcelnook.com.au Front page Re-Design

We need a front page redesign for the website parcelnook.com.au,
The site needs to keep a number of products products highlighted on the front page. Same buttons but navigation could be different and we still need some text for SEO.
What we do not currently like:
1. The big banners.
2. The use of too much orange especially the 50% orange borders.
3. the fact that products cannot be seen straight away when logged-in.
4. The fact that it is hard to convert to tablet friendly
5. The fact that it's not a modern design.

What we think we want:

1. Maybe more use of 1 colour (purple or orange) with the other a secondary highlight colour.
2. A more modern look
3. The wow factor

Look at parcelnook.com.au take the elements that you need and design.
Updates

Reason: Designs are getting better. liking the designs that don't look like the usual e-commerce templates out there.

Hello,

We are making decisions next Monday. Sorry for the delay but there has been a lot of holidays in Australia and decision makers away.

Industry/Entity Type

Seo

Colors
6b449b
f78f20
ffffff

```html
<!DOCTYPE html>
<html lang="en">
<head>
<meta charset="utf-8">
<title>Parcelnook.com.au – Gift Baskets &amp; Hampers</title>
<link href="https://fonts.googleapis.com/css2?family=Open+Sans:wght@400;600;700;800&display=swap" rel="stylesheet">
<style>
:root{
  --purple:#912d8f;
  --purple-dark:#6e1f6d;
  --orange:#f78f20;
  --orange-dark:#e2760b;
  --ink:#333;
  --muted:#777;
  --line:#dcdcdc;
  --soft:#f3f3f3;
  --white:#fff;
}
*{box-sizing:border-box;margin:0;padding:0}
html,body{width:1200px;height:2839px;overflow:hidden;background:var(--white)}
body{position:relative;font-family:"Open Sans",Arial,sans-serif;color:var(--ink)}
a{color:inherit;text-decoration:none}
ul{list-style:none}
.abs{position:absolute}

/* utility bar */
.utility-bar{left:0;top:0;width:1200px;height:47px;background:var(--soft);border-bottom:1px solid #e6e6e6}
.utility-bar .inner{position:absolute;left:112px;right:112px;top:0;height:47px;display:flex;align-items:center;justify-content:space-between;font-size:12px;color:var(--muted)}
.utility-bar .prefs{display:flex;gap:22px;align-items:center}
.utility-bar .prefs span{display:flex;align-items:center;gap:6px}
.utility-bar .dot{width:14px;height:14px;border-radius:50%;background:#999}
.utility-bar .links{display:flex;gap:34px}

/* header */
.brand{left:122px;top:66px;display:flex;align-items:center;gap:12px}
.brand .mark{width:54px;height:54px;background:var(--orange)}
.brand .name{font-size:42px;font-weight:800;color:var(--purple);line-height:1}
.brand-tag{left:126px;top:160px;font-size:14px;font-weight:700;color:var(--purple)}
.contact-line{top:84px;display:flex;align-items:center;gap:14px;font-size:15px;color:#555}
.contact-line svg{display:block}
.search{left:593px;top:125px;width:328px;height:42px;display:flex}
.search .field{flex:1;border:1px solid var(--line);background:#f7f7f7;font-size:12px;color:#999;padding:12px 14px}
.search .go{width:96px;background:var(--purple);color:var(--white);font-size:16px;font-weight:600;display:flex;align-items:center;justify-content:center}
.cart-btn{left:928px;top:125px;width:152px;height:42px;background:var(--orange);color:var(--white);font-size:13px;font-weight:600;display:flex;align-items:center;justify-content:center;gap:7px;border-radius:2px;white-space:nowrap}

/* navigation */
.main-nav{left:110px;top:199px;width:980px;height:57px;background:var(--orange);display:flex}
.main-nav a{flex:auto;display:flex;align-items:center;justify-content:center;color:var(--white);font-size:14px;white-space:nowrap}
.main-nav a.active{background:var(--orange-dark)}

/* hero */
.hero{left:110px;top:256px;width:980px;height:410px;background:radial-gradient(ellipse at 72% 55%,#f3e7cf 0%,#d9c09a 30%,#a8784a 62%,#6e4a2c 100%)}
.hero-copy{left:157px;top:338px;width:440px;color:var(--white)}
.hero-copy h1{font-size:32px;font-weight:400;margin-bottom:8px;white-space:nowrap}
.hero-copy .sub{font-size:17px;margin-bottom:16px;white-space:nowrap}
.hero-copy .lorem{width:320px;font-size:12px;line-height:21px;color:#f1e6dc}
.join-btn{left:160px;top:535px;width:138px;height:44px;background:var(--orange);color:#3a2205;font-size:18px;font-weight:600;display:flex;align-items:center;justify-content:center;border-radius:3px}

/* welcome band */
.welcome{left:110px;top:666px;width:980px;height:148px;background:var(--purple)}
.welcome .frame{position:absolute;left:17px;top:15px;width:946px;height:118px;border:3px solid var(--white)}
.welcome h2{position:absolute;left:32px;top:50px;font-size:26px;font-weight:700;color:var(--white);white-space:nowrap;line-height:1.3}
.welcome p{position:absolute;left:266px;top:54px;width:500px;font-size:12px;line-height:19px;color:var(--white)}
.welcome .more{position:absolute;left:787px;top:55px;width:156px;height:38px;background:var(--orange);color:#3a2205;font-size:17px;font-weight:600;display:flex;align-items:center;justify-content:center;border-radius:3px}

/* products */
.section-title{left:122px;top:836px;font-size:24px;color:var(--orange)}
.tabs{left:112px;top:890px;width:980px;height:56px;border:1px solid var(--line);display:flex}
.tabs a{display:flex;align-items:center;justify-content:center;font-size:17px;color:#555;border-right:1px solid var(--line)}
.tabs a:nth-child(1){width:112px;color:var(--purple)}
.tabs a:nth-child(2){width:126px}
.tabs a:nth-child(3){width:121px}

.card{width:214px;height:303px;border:2px solid var(--line);background:var(--white)}
.card.featured{border-color:var(--purple)}
.card .photo{position:absolute;left:8px;top:8px;width:194px;height:186px}
.card .ribbon{position:absolute;right:-2px;top:-2px}
.card .title{position:absolute;left:10px;top:214px;width:194px;font-size:12px;color:#333;white-space:nowrap;line-height:16px}
.card .stars{position:absolute;left:10px;top:237px;font-size:17px;line-height:20px;letter-spacing:1px;color:var(--orange)}
.card .stars i{font-style:normal;color:#999}
.card .price{position:absolute;left:10px;top:268px;font-size:14px;color:var(--orange)}
.card .add{position:absolute;right:8px;top:262px;width:84px;height:26px;background:var(--orange);color:var(--white);font-size:12px;font-weight:600;display:flex;align-items:center;justify-content:center;border-radius:3px;white-space:nowrap}

/* shop boxes */
.panel{top:2003px;height:231px;border:1px solid var(--line);border-radius:6px 6px 0 0;overflow:hidden}
.panel h3{height:38px;background:var(--purple);color:var(--white);font-size:12px;font-weight:700;padding:12px 14px}
.panel li{height:31px;font-size:12px;color:#555;padding:8px 14px;border-bottom:1px solid #e9e9e9}
.panel li:nth-child(odd){background:#f5f5f5}
.specials{position:absolute;left:22px;top:58px;width:440px;display:grid;grid-template-columns:1fr 1fr;row-gap:22px}
.special{display:flex;gap:14px}
.special .thumb{width:52px;height:44px;background:radial-gradient(circle,#f3a6c8,#e9d2e0 60%,#fff)}
.special p{font-size:12px;line-height:15px;color:#666}
.special .now{font-size:17px;font-weight:700;color:var(--orange)}
.special .was{font-size:17px;font-weight:700;color:var(--purple);text-decoration:line-through;margin-left:6px}

/* promo tiles */
.promo{top:2275px;height:154px;display:flex;flex-direction:column;align-items:center;justify-content:center;text-align:center}
.promo.guarantee{left:122px;width:292px;border:4px solid var(--purple)}
.promo.deals{left:786px;width:293px;border:4px solid var(--orange)}
.promo .big{font-size:24px;font-weight:700;line-height:26px;white-space:nowrap}
.promo .small{font-size:24px;color:#666;line-height:26px}
.guarantee .big{color:var(--purple)}
.deals .big{color:var(--orange-dark)}
.support{left:434px;top:2275px;width:333px;height:154px;background:linear-gradient(90deg,#7b2279,#a0479d)}
.support .agent{position:absolute;right:0;top:0;width:128px;height:154px;background:linear-gradient(160deg,#e9e3ea,#c9b8c8)}
.support h4{position:absolute;left:18px;top:14px;font-size:26px;font-weight:800;color:var(--white);white-space:nowrap}
.support p{position:absolute;left:18px;top:50px;font-size:13px;line-height:17px;color:var(--white)}
.support .chat{position:absolute;left:16px;top:96px;width:134px;height:36px;background:var(--orange);color:var(--white);font-size:20px;font-weight:800;display:flex;align-items:center;justify-content:center;border-radius:3px}

/* footer */
.footer-rule{left:0;top:2465px;width:1200px;height:1px;background:var(--line)}
.foot-col{top:2510px}
.foot-col h5{font-size:21px;font-weight:400;color:#222;margin-bottom:18px;white-space:nowrap}
.foot-col li{font-size:13px;color:#555;height:24px;white-space:nowrap}
.foot-col li b{color:var(--purple);font-weight:700;margin-right:12px;font-size:11px}
.foot-brand{display:flex;align-items:center;gap:8px;margin-bottom:14px}
.foot-brand .mark{width:26px;height:26px;background:var(--orange)}
.foot-brand .name{font-size:24px;font-weight:800;color:var(--purple)}
.foot-about p{font-size:12px;line-height:23px;color:#444}
.contact li{display:flex;align-items:center;gap:10px}
.socials{display:flex;gap:8px;margin-top:12px}
.socials span{width:34px;height:34px;border-radius:50%}
.bottom-rule{left:112px;top:2781px;width:976px;height:1px;background:var(--line)}
.copyright{left:112px;top:2800px;font-size:11px;color:#555}
.payments{left:946px;top:2795px;display:flex;gap:6px}
.payments span{width:44px;height:28px;border-radius:3px;border:1px solid #ccc}
</style>
</head>
<body>

<div class="abs utility-bar">
  <div class="inner">
    <div class="prefs">
      <span><i class="dot"></i>Currency: USD ▾</span>
      <span><i class="dot"></i>Language: English ▾</span>
    </div>
    <nav class="links"><a>My Account</a><a>Wishlist</a><a>My Cart</a><a>Checkout</a><a>Log In</a></nav>
  </div>
</div>

<div class="abs brand"><span class="mark"></span><span class="name">parcelnook</span></div>
<div class="abs brand-tag">parcel nook &amp; hamper network</div>

<div class="abs contact-line" style="left:700px">
  <svg width="16" height="16" viewBox="0 0 24 24"><path fill="#912d8f" d="M6.6 10.8a15 15 0 0 0 6.6 6.6l2.2-2.2c.3-.3.7-.4 1-.2 1.1.4 2.3.6 3.6.6.6 0 1 .4 1 1V20c0 .6-.4 1-1 1A17 17 0 0 1 3 4c0-.6.4-1 1-1h3.5c.6 0 1 .4 1 1 0 1.3.2 2.5.6 3.6.1.3 0 .7-.2 1z"/></svg>
  <span>1300 555 018</span>
</div>
<div class="abs contact-line" style="left:870px">
  <svg width="18" height="14" viewBox="0 0 18 14"><rect width="18" height="14" rx="1" fill="#912d8f"/><path d="M1 1l8 6 8-6" stroke="#fff" stroke-width="1.5" fill="none"/></svg>
  <span>help@parcelnook.com.au</span>
</div>

<div class="abs search"><div class="field">Search...</div><div class="go">Search</div></div>
<div class="abs cart-btn">
  <svg width="16" height="14" viewBox="0 0 16 14"><path d="M0 1h3l2 8h9l2-6H4" stroke="#fff" stroke-width="1.6" fill="none"/><circle cx="6" cy="12" r="1.4" fill="#fff"/><circle cx="13" cy="12" r="1.4" fill="#fff"/></svg>
  Shopping Cart (0)
</div>

<nav class="abs main-nav">
  <a class="active">Easter</a><a>Mothers Day</a><a>Get Well</a><a>Thank You</a><a>Birthday</a><a>Anniversary</a><a>Romance</a><a>New Baby</a><a>Childrens</a><a>For Him</a><a>For Her</a>
</nav>

<div class="abs hero" role="img" aria-label="Photo of a cream plush teddy bear wearing a ribbon"></div>
<div class="abs hero-copy">
  <h1>Teddy Bears &amp; Toys</h1>
  <p class="sub">Teddy Bears and Gifts including gorgeous plush toys</p>
  <p class="lorem">Lorem ipsum dolor sit amet, consectetuer adipiscing elit, sed diam nonummy nibh euismod tincidunt ut laoreet dolore magna aliquam erat volutpat. Ut wisi enim ad minim venia...</p>
</div>
<a class="abs join-btn">Join Now</a>

<section class="abs welcome">
  <div class="frame"></div>
  <h2>First Time Here?</h2>
  <p>Parcel Nook baskets and hampers great range is now available with Gift Delivery Australia Wide! Send a gift Australia wide today. Fast delivery.</p>
  <a class="more">Find Out More</a>
</section>

<h2 class="abs section-title" style="font-weight:400">Todays Top Products</h2>
<div class="abs tabs"><a>Ocassional</a><a>Latest</a><a>Most Viewed</a></div>

<!-- product grid -->
<div class="abs card" style="left:123px;top:977px">
  <div class="photo" role="img" aria-label="Stacked white gift boxes with purple ribbons" style="background:radial-gradient(circle,#b9a3cf,#ece6f1 55%,#fff 80%)"></div>
  <svg class="ribbon" width="74" height="74" viewBox="0 0 74 74"><polygon points="20,0 46,0 74,28 74,54" fill="#912d8f"/><text x="53.5" y="23" font-size="8" fill="#fff" font-family="Open Sans" transform="rotate(45 53.5 20.5)" text-anchor="middle">Gift Ideas</text></svg>
  <div class="title">Tower Of Deliciousness</div><div class="stars">★★★★<i>☆</i></div><div class="price">$54.95</div><a class="add">Add To Cart</a>
</div>
<div class="abs card featured" style="left:373px;top:977px">
  <div class="photo" role="img" aria-label="Wooden crate with two bottles of wine" style="background:radial-gradient(circle,#a98a6a,#e8ddcf 55%,#fff 80%)"></div>
  <svg class="ribbon" width="74" height="74" viewBox="0 0 74 74"><polygon points="20,0 46,0 74,28 74,54" fill="#912d8f"/><text x="53.5" y="23" font-size="8" fill="#fff" font-family="Open Sans" transform="rotate(45 53.5 20.5)" text-anchor="middle">Gift Ideas</text></svg>
  <div class="title">Elmvale Chardonnay &amp; Shiraz</div><div class="stars">★★★★<i>☆</i></div><div class="price">$54.95</div><a class="add">Add To Cart</a>
</div>
<div class="abs card" style="left:619px;top:977px">
  <div class="photo" role="img" aria-label="Basket of fresh fruit" style="background:radial-gradient(circle,#d9563a,#f1c08a 50%,#fff 80%)"></div>
  <svg class="ribbon" width="74" height="74" viewBox="0 0 74 74"><polygon points="20,0 46,0 74,28 74,54" fill="#912d8f"/><text x="53.5" y="23" font-size="8" fill="#fff" font-family="Open Sans" transform="rotate(45 53.5 20.5)" text-anchor="middle">Gift Ideas</text></svg>
  <div class="title">Fruity Goodness</div><div class="stars">★★★★<i>☆</i></div><div class="price">$54.95</div><a class="add">Add To Cart</a>
</div>
<div class="abs card" style="left:865px;top:977px">
  <div class="photo" role="img" aria-label="Gift chest with wine and cheese" style="background:radial-gradient(circle,#5a3b6e,#d9cfe0 55%,#fff 80%)"></div>
  <svg class="ribbon" width="74" height="74" viewBox="0 0 74 74"><polygon points="20,0 46,0 74,28 74,54" fill="#912d8f"/><text x="53.5" y="23" font-size="8" fill="#fff" font-family="Open Sans" transform="rotate(45 53.5 20.5)" text-anchor="middle">Gift Ideas</text></svg>
  <div class="title">Chalk And Cheese Gift Chest</div><div class="stars">★★★★<i>☆</i></div><div class="price">$54.95</div><a class="add">Add To Cart</a>
</div>

<div class="abs card" style="left:123px;top:1318px">
  <div class="photo" role="img" aria-label="Tropical fruit and flower arrangement" style="background:radial-gradient(circle,#e9892f,#f3d39c 50%,#fff 80%)"></div>
  <svg class="ribbon" width="74" height="74" viewBox="0 0 74 74"><polygon points="20,0 46,0 74,28 74,54" fill="#912d8f"/><text x="53.5" y="23" font-size="8" fill="#fff" font-family="Open Sans" transform="rotate(45 53.5 20.5)" text-anchor="middle">Gift Ideas</text></svg>
  <div class="title">The Tropicana</div><div class="stars">★★★★<i>☆</i></div><div class="price">$54.95</div><a class="add">Add To Cart</a>
</div>
<div class="abs card" style="left:373px;top:1318px">
  <div class="photo" role="img" aria-label="Wooden crate with two bottles of wine" style="background:radial-gradient(circle,#a98a6a,#e8ddcf 55%,#fff 80%)"></div>
  <svg class="ribbon" width="74" height="74" viewBox="0 0 74 74"><polygon points="20,0 46,0 74,28 74,54" fill="#912d8f"/><text x="53.5" y="23" font-size="8" fill="#fff" font-family="Open Sans" transform="rotate(45 53.5 20.5)" text-anchor="middle">Gift Ideas</text></svg>
  <div class="title">Elmvale Sauvignon &amp; Merlot</div><div class="stars">★★★★<i>☆</i></div><div class="price">$54.95</div><a class="add">Add To Cart</a>
</div>
<div class="abs card" style="left:619px;top:1318px">
  <div class="photo" role="img" aria-label="Bouquet of wrapped chocolates" style="background:radial-gradient(circle,#b8892e,#e8d6a8 50%,#fff 80%)"></div>
  <svg class="ribbon" width="74" height="74" viewBox="0 0 74 74"><polygon points="20,0 46,0 74,28 74,54" fill="#912d8f"/><text x="53.5" y="23" font-size="8" fill="#fff" font-family="Open Sans" transform="rotate(45 53.5 20.5)" text-anchor="middle">Gift Ideas</text></svg>
  <div class="title">Hazel Crunch Bouquet</div><div class="stars">★★★★<i>☆</i></div><div class="price">$54.95</div><a class="add">Add To Cart</a>
</div>
<div class="abs card" style="left:865px;top:1318px">
  <div class="photo" role="img" aria-label="Gift crate with cream liqueur and glasses" style="background:radial-gradient(circle,#8a6a4c,#e5d9c9 55%,#fff 80%)"></div>
  <svg class="ribbon" width="74" height="74" viewBox="0 0 74 74"><polygon points="20,0 46,0 74,28 74,54" fill="#912d8f"/><text x="53.5" y="23" font-size="8" fill="#fff" font-family="Open Sans" transform="rotate(45 53.5 20.5)" text-anchor="middle">Gift Ideas</text></svg>
  <div class="title">Velvet Irish Cream Gift Set</div><div class="stars">★★★★<i>☆</i></div><div class="price">$54.95</div><a class="add">Add To Cart</a>
</div>

<div class="abs card" style="left:123px;top:1658px">
  <div class="photo" role="img" aria-label="Gift crate with tawny port and treats" style="background:radial-gradient(circle,#7a4a32,#e3d3c5 55%,#fff 80%)"></div>
  <svg class="ribbon" width="74" height="74" viewBox="0 0 74 74"><polygon points="20,0 46,0 74,28 74,54" fill="#912d8f"/><text x="53.5" y="23" font-size="8" fill="#fff" font-family="Open Sans" transform="rotate(45 53.5 20.5)" text-anchor="middle">Gift Ideas</text></svg>
  <div class="title">Redgum Club Tawny Gift Set</div><div class="stars">★★★★<i>☆</i></div><div class="price">$54.95</div><a class="add">Add To Cart</a>
</div>
<div class="abs card" style="left:373px;top:1658px">
  <div class="photo" role="img" aria-label="Plush bunny with Easter eggs in a crate" style="background:radial-gradient(circle,#e9e4ea,#cfe3f0 50%,#fff 80%)"></div>
  <svg class="ribbon" width="74" height="74" viewBox="0 0 74 74"><polygon points="20,0 46,0 74,28 74,54" fill="#912d8f"/><text x="53.5" y="23" font-size="8" fill="#fff" font-family="Open Sans" transform="rotate(45 53.5 20.5)" text-anchor="middle">Gift Ideas</text></svg>
  <div class="title">Fluffy Bunny Easter Egg Gift</div><div class="stars">★★★★<i>☆</i></div><div class="price">$54.95</div><a class="add">Add To Cart</a>
</div>
<div class="abs card" style="left:619px;top:1658px">
  <div class="photo" role="img" aria-label="Plush chicken on a pot of Easter eggs" style="background:radial-gradient(circle,#f5e7a8,#f4d2c4 50%,#fff 80%)"></div>
  <svg class="ribbon" width="74" height="74" viewBox="0 0 74 74"><polygon points="20,0 46,0 74,28 74,54" fill="#912d8f"/><text x="53.5" y="23" font-size="8" fill="#fff" font-family="Open Sans" transform="rotate(45 53.5 20.5)" text-anchor="middle">Gift Ideas</text></svg>
  <div class="title">Fluffy Chicken Easter Egg Gift</div><div class="stars">★★★★<i>☆</i></div><div class="price">$54.95</div><a class="add">Add To Cart</a>
</div>
<div class="abs card" style="left:865px;top:1658px">
  <div class="photo" role="img" aria-label="Chocolate rabbit in an orange gift box" style="background:radial-gradient(circle,#6d93b8,#eccaa0 55%,#fff 80%)"></div>
  <svg class="ribbon" width="74" height="74" viewBox="0 0 74 74"><polygon points="20,0 46,0 74,28 74,54" fill="#912d8f"/><text x="53.5" y="23" font-size="8" fill="#fff" font-family="Open Sans" transform="rotate(45 53.5 20.5)" text-anchor="middle">Gift Ideas</text></svg>
  <div class="title">Rabbit Chocolate Easter Box</div><div class="stars">★★★★<i>☆</i></div><div class="price">$54.95</div><a class="add">Add To Cart</a>
</div>

<!-- shop panels -->
<div class="abs panel" style="left:122px;width:226px">
  <h3>SHOP BY BASKET PRICE</h3>
  <ul><li>Gifts Under $50</li><li>Gifts $50 to $75</li><li>Gifts $75 to $100</li><li>Gifts $100 to $150</li><li>Gifts Over $150</li><li>Gifts Over $170</li></ul>
</div>
<div class="abs panel" style="left:362px;width:475px">
  <h3>SPECIALS</h3>
  <div class="specials">
    <div class="special"><div class="thumb" role="img" aria-label="Pink flower arrangement"></div><div><p>Lorem ipsum dolor<br>sit amet.</p><span class="now">$3.99</span><span class="was">$12.99</span></div></div>
    <div class="special"><div class="thumb" role="img" aria-label="Pink flower arrangement"></div><div><p>Lorem ipsum dolor<br>sit amet.</p><span class="now">$3.99</span><span class="was">$12.99</span></div></div>
    <div class="special"><div class="thumb" role="img" aria-label="Pink flower arrangement"></div><div><p>Lorem ipsum dolor<br>adipiscing elit</p><span class="now">$3.99</span><span class="was">$12.99</span></div></div>
    <div class="special"><div class="thumb" role="img" aria-label="Pink flower arrangement"></div><div><p>Lorem ipsum dolor<br>adipiscing elit</p><span class="now">$3.99</span><span class="was">$12.99</span></div></div>
  </div>
</div>
<div class="abs panel" style="left:853px;width:226px">
  <h3>SHOP BY OCCASSIONS</h3>
  <ul><li>Easter Gifts</li><li>Mothers Day Gifts</li><li>Fathers Day Gifts</li><li>Christmas Gifts</li><li>Valentines Day Gifts</li><li>Thanks Giving</li></ul>
</div>

<!-- promo tiles -->
<div class="abs promo guarantee">
  <svg width="60" height="54" viewBox="0 0 60 54"><path d="M30 52 4 26A14 14 0 0 1 30 8a14 14 0 0 1 26 18z" fill="#912d8f"/></svg>
  <div class="big" style="margin-top:8px">100% SATISFACTION</div>
  <div class="small">GUARANTEED</div>
</div>
<div class="abs support">
  <div class="agent" role="img" aria-label="Photo of a support agent wearing a headset"></div>
  <h4>LIVE SUPPORT</h4>
  <p>Online Now Click below<br>button to start a chat</p>
  <a class="chat">CHAT NOW</a>
</div>
<div class="abs promo deals">
  <svg width="48" height="48" viewBox="0 0 48 48"><rect x="4" y="16" width="40" height="10" fill="#f78f20"/><rect x="8" y="26" width="32" height="20" fill="#f78f20"/><rect x="21" y="16" width="6" height="30" fill="#fff"/><path d="M24 16C18 4 8 8 14 16M24 16c6-12 16-8 10 0" stroke="#f78f20" stroke-width="3" fill="none"/></svg>
  <div class="big" style="margin-top:6px">GREAT DAILY DEALS</div>
  <div class="small">SHOP NOW!</div>
</div>

<!-- footer -->
<div class="abs footer-rule"></div>

<div class="abs foot-col foot-about" style="left:112px;width:240px">
  <h5>About Parcel Nook</h5>
  <div class="foot-brand"><span class="mark"></span><span class="name">parcelnook</span></div>
  <p>Gift baskets delivered Australia wide! Gift ideas for Easter, Mother's day, birthdays, new babies and more. Gourmet gift baskets and hampers</p>
</div>
<div class="abs foot-col" style="left:418px">
  <h5>Site Links</h5>
  <ul><li><b>&gt;&gt;</b>Easter</li><li><b>&gt;&gt;</b>Mothers Day</li><li><b>&gt;&gt;</b>Get Well</li><li><b>&gt;&gt;</b>Thank You</li><li><b>&gt;&gt;</b>Birthday</li><li><b>&gt;&gt;</b>Anniversary</li><li><b>&gt;&gt;</b>Romance</li><li><b>&gt;&gt;</b>New Baby</li></ul>
</div>
<div class="abs foot-col" style="left:634px">
  <h5>My Account</h5>
  <ul><li><b>&gt;&gt;</b>About Us</li><li><b>&gt;&gt;</b>Customer Service</li><li><b>&gt;&gt;</b>Privacy Policy</li><li><b>&gt;&gt;</b>Sitemap</li><li><b>&gt;&gt;</b>Terms &amp; Conditions</li><li><b>&gt;&gt;</b>Advanced Search</li></ul>
</div>
<div class="abs foot-col contact" style="left:832px">
  <h5>Contact Us</h5>
  <ul>
    <li><svg width="14" height="12" viewBox="0 0 14 12"><rect x="1" y="1" width="12" height="10" rx="1" fill="none" stroke="#912d8f" stroke-width="1.5"/></svg>Web : http:// www.parcelnook.com.au</li>
    <li><svg width="14" height="12" viewBox="0 0 14 12"><rect width="14" height="11" fill="#912d8f"/><path d="M1 1l6 5 6-5" stroke="#fff" fill="none"/></svg>Email : help@parcelnook.com.au</li>
    <li><svg width="14" height="14" viewBox="0 0 24 24"><path fill="#912d8f" d="M6.6 10.8a15 15 0 0 0 6.6 6.6l2.2-2.2c.3-.3.7-.4 1-.2 1.1.4 2.3.6 3.6.6.6 0 1 .4 1 1V20c0 .6-.4 1-1 1A17 17 0 0 1 3 4c0-.6.4-1 1-1h3.5c.6 0 1 .4 1 1 0 1.3.2 2.5.6 3.6.1.3 0 .7-.2 1z"/></svg>National : 1300 555 018</li>
    <li><svg width="14" height="14" viewBox="0 0 24 24"><path fill="#912d8f" d="M6.6 10.8a15 15 0 0 0 6.6 6.6l2.2-2.2c.3-.3.7-.4 1-.2 1.1.4 2.3.6 3.6.6.6 0 1 .4 1 1V20c0 .6-.4 1-1 1A17 17 0 0 1 3 4c0-.6.4-1 1-1h3.5c.6 0 1 .4 1 1 0 1.3.2 2.5.6 3.6.1.3 0 .7-.2 1z"/></svg>International : +61 1300 555 018</li>
  </ul>
  <div class="socials"><span style="background:#f39c2c"></span><span style="background:#3fb3c9"></span><span style="background:#3b5b9a"></span><span style="background:#dd4b39"></span><span style="background:#4aa6e0"></span></div>
</div>

<div class="abs bottom-rule"></div>
<div class="abs copyright">© 2014 Parcel Nook &nbsp;|&nbsp; All Rights Reserved</div>
<div class="abs payments"><span style="background:#e9eef7"></span><span style="background:#f7ece4"></span><span style="background:#f2f2f2"></span></div>

</body>
</html>
```